Coastal Bright Sweep Business Card

We are a cleaning and waste management company with the slogan "making waste to landfill a thing of the past". We would like a re-design of our current business card. On the front we want to continue to use our logo as the focus point. On the back, we want the whole thing re-done to be less busy. We want the staff member’s name, the job title, mobile number, email and website. We do not want the address on the card. We still want the green, black and blue colours used, but a new font for the information on the back. Please do not change the logo design at all. We are also thinking about using icons to replace the text ‘mobile, email, website’. The “events + commercial” banner needs to be incorporated somewhere and needs to read “events + commercial + waste”. Another important point for consideration is that we are very concerned about being environmentally sustainable and will be printing on recycled paper. All designs should be made to compliment this in regards to boldness and colouring. Please find attached our logo, our colour chart and an image of our current business card.

```html
<!DOCTYPE html>
<html lang="en">
<head>
<meta charset="utf-8">
<title>Coastal Bright Sweep Business Card</title>
<link rel="stylesheet" href="https://fonts.googleapis.com/css2?family=Roboto+Condensed:wght@400;700&family=Work+Sans:wght@400;700&display=swap">
<style>
  :root {
    --navy: #173f73;
    --green: #7dc242;
    --blue: #29abe2;
    --ink: #555555;
    --paper: #ffffff;
    --backdrop: #e8e5e0;
  }
  * { margin: 0; padding: 0; box-sizing: border-box; }
  html, body {
    width: 1200px;
    height: 930px;
    overflow: hidden;
    background: var(--backdrop);
  }
  .card {
    position: absolute;
    left: 278px;
    width: 644px;
    height: 368px;
    border-radius: 22px;
    overflow: hidden;
    box-shadow: 0 4px 14px rgba(0,0,0,0.18);
  }
  .card--front { top: 76px; background: var(--paper); }
  .card--back { top: 486px; background: var(--green); }

  /* front */
  .brand-name {
    position: absolute;
    font-family: "Work Sans", sans-serif;
    font-weight: 700;
    line-height: 1.0;
    text-align: center;
  }
  .card--front .brand-name {
    left: 52px;
    top: 134px;
    width: 190px;
    font-size: 31px;
    color: var(--navy);
  }
  .divider {
    position: absolute;
    left: 280px;
    top: 134px;
    width: 2px;
    height: 106px;
    background: var(--navy);
  }
  .contact {
    position: absolute;
    left: 318px;
    top: 126px;
    font-family: "Roboto Condensed", sans-serif;
  }
  .contact__name {
    font-size: 30px;
    font-weight: 700;
    line-height: 1;
    color: var(--navy);
    letter-spacing: -0.3px;
  }
  .contact__name .surname { color: var(--green); }
  .contact__role {
    margin-top: 4px;
    font-size: 16px;
    color: var(--navy);
  }
  .contact__list {
    list-style: none;
    margin-top: 12px;
  }
  .contact__item {
    display: flex;
    align-items: center;
    height: 20px;
    font-size: 16px;
    color: var(--ink);
  }
  .contact__item svg {
    width: 10px;
    height: 10px;
    margin: 0 10px 0 2px;
    flex: none;
  }
  .contact__item .domain { color: var(--navy); }
  .service-band {
    position: absolute;
    left: 0;
    bottom: 0;
    width: 644px;
    height: 30px;
  }
  .service-band__label {
    position: absolute;
    left: 136px;
    bottom: 0;
    width: 374px;
    height: 30px;
    line-height: 30px;
    text-align: center;
    font-family: "Work Sans", sans-serif;
    font-size: 18px;
    letter-spacing: 0.6px;
    color: var(--paper);
  }

  /* back */
  .card--back .brand-name {
    left: 0;
    top: 92px;
    width: 644px;
    font-size: 56px;
    color: var(--paper);
  }
  .tagline {
    position: absolute;
    left: 0;
    top: 325px;
    width: 644px;
    text-align: center;
    font-family: "Work Sans", sans-serif;
    font-size: 19px;
    letter-spacing: 1px;
    color: var(--paper);
  }
</style>
</head>
<body>

<section class="card card--front">
  <p class="brand-name">Coastal<br>Bright<br>Sweep</p>
  <div class="divider"></div>

  <div class="contact">
    <h1 class="contact__name">MORGAN <span class="surname">TULLY</span></h1>
    <p class="contact__role">Client Manager</p>
    <ul class="contact__list">
      <li class="contact__item">
        <svg viewBox="0 0 10 10" aria-hidden="true"><path d="M2.2 0.8 L3.6 2.6 L2.8 3.6 Q3.8 5.8 6.2 7.2 L7.2 6.4 L9 7.8 L8 9.2 Q3.6 8.6 0.8 2 Z" fill="none" stroke="var(--navy)" stroke-width="1"/></svg>
        0400 555 218
      </li>
      <li class="contact__item">
        <svg viewBox="0 0 10 10" aria-hidden="true"><rect x="0.6" y="2" width="8.8" height="6" fill="none" stroke="var(--navy)" stroke-width="1"/><path d="M0.6 2 L5 5.6 L9.4 2" fill="none" stroke="var(--navy)" stroke-width="1"/></svg>
        mtully@coastalbrightsweep.com.au
      </li>
      <li class="contact__item">
        <svg viewBox="0 0 10 10" aria-hidden="true"><circle cx="5" cy="5" r="4.3" fill="none" stroke="var(--navy)" stroke-width="0.9"/><ellipse cx="5" cy="5" rx="1.9" ry="4.3" fill="none" stroke="var(--navy)" stroke-width="0.9"/><path d="M0.7 5 H9.3 M1.4 2.8 H8.6 M1.4 7.2 H8.6" stroke="var(--navy)" stroke-width="0.8"/></svg>
        <span>www.<span class="domain">coastalbrightsweep</span>.com.au</span>
      </li>
    </ul>
  </div>

  <svg class="service-band" viewBox="0 0 644 30" aria-hidden="true">
    <polygon points="0,0 130,0 153,30 0,30" fill="var(--green)"/>
    <polygon points="135,0 486,0 510,30 158,30" fill="var(--navy)"/>
    <polygon points="491,0 644,0 644,30 516,30" fill="var(--blue)"/>
  </svg>
  <p class="service-band__label">Events + commercial + waste</p>
</section>

<section class="card card--back">
  <p class="brand-name">Coastal<br>Bright<br>Sweep</p>
  <p class="tagline">MAKING WASTE TO LANDFILL A THING OF THE PAST</p>
</section>

</body>
</html>
```